Kelvard Engineers: Why you should hire us keepsake

New design. Open to plastic cards. We are an engineering firm that designs cell phone towers and commercial buildings. Please check out our website www.kelvardeng.example for more details. We want people to remember our card and for it to be useful if possible. We want the same look and feel on these cards to be translated to other marketing material we may need such as brochures.

Target Market(s)

Architects, Developers and Telecommunication Carriers

Industry/Entity Type

Engineering

Contact Information for Business Card

Card with our company colors, logo, and innovative design with elements related to our industry.

Font styles to use
Sans Serif

Colors
9bcb3c
abd036
0255a3

Requirements
Must have
• Sleek and hip design
Nice to have
• Bright lime green and navy coloring that pops with an innovative design.
Should not have
• A basic and boring design

```html
<!DOCTYPE html>
<html lang="en">
<head>
<meta charset="utf-8">
<title>Kelvard Engineers – Business Card</title>
<link rel="stylesheet" href="https://fonts.googleapis.com/css2?family=Montserrat:wght@600;700;800&display=swap">
<style>
  :root {
    --navy: #1d3461;
    --lime: #6cbd45;
    --white: #ffffff;
    --stage: #111111;
  }
  * { margin: 0; padding: 0; box-sizing: border-box; }
  html, body {
    width: 1200px; height: 1000px; overflow: hidden;
    background: var(--stage);
    font-family: "Montserrat", sans-serif;
  }
  .stage { position: relative; width: 1200px; height: 1000px; }
  .card {
    position: absolute; top: 357px;
    width: 500px; height: 286px;
    border-radius: 18px; overflow: hidden;
  }
  .card-back { left: 70px; background: var(--navy); display: flex; align-items: center; justify-content: center; }
  .card-back .brand-name { font-size: 64px; font-weight: 800; color: var(--lime); letter-spacing: -1px; }
  .card-front { left: 630px; background: var(--white); color: var(--navy); }
  .block { position: absolute; }
  .block-navy { background: var(--navy); }
  .block-lime { background: var(--lime); }
  .brand {
    position: absolute; right: 30px; top: 52px; text-align: right;
  }
  .brand .brand-name { display: block; font-size: 50px; font-weight: 800; color: var(--lime); line-height: 1; letter-spacing: -1px; }
  .brand .tagline { display: block; font-size: 12.5px; font-weight: 700; color: var(--navy); margin-top: 4px; }
  .person-name { position: absolute; left: 28px; top: 138px; font-size: 18px; font-weight: 600; }
  .contact-list { position: absolute; left: 28px; top: 168px; list-style: none; }
  .contact-list li { display: flex; align-items: center; gap: 8px; font-size: 12px; font-weight: 600; line-height: 19px; }
  .contact-list svg { width: 11px; height: 11px; fill: var(--lime); flex: none; }
  .web-row { position: absolute; left: 28px; top: 238px; display: flex; align-items: center; gap: 14px; font-size: 12.5px; font-weight: 700; }
  .divider { width: 2px; height: 20px; background: var(--navy); }
</style>
</head>
<body>
<main class="stage">
  <section class="card card-back" aria-label="Card back">
    <span class="brand-name">Kelvard</span>
  </section>

  <section class="card card-front" aria-label="Card front">
    <div class="block block-navy" style="left:36px;top:0;width:58px;height:32px"></div>
    <div class="block block-lime" style="left:18px;top:48px;width:44px;height:40px"></div>
    <div class="block block-lime" style="left:72px;top:34px;width:50px;height:44px"></div>

    <div class="block block-lime" style="left:360px;top:184px;width:62px;height:58px"></div>
    <div class="block block-lime" style="left:432px;top:170px;width:44px;height:40px"></div>
    <div class="block block-navy" style="left:420px;top:222px;width:80px;height:64px"></div>

    <div class="brand">
      <span class="brand-name">Kelvard</span>
      <span class="tagline">Multi-discipline engineering</span>
    </div>

    <h1 class="person-name">Dana Marlow Pruett</h1>
    <ul class="contact-list">
      <li><svg viewBox="0 0 24 24" aria-hidden="true"><path d="M6.6 10.8a15 15 0 0 0 6.6 6.6l2.2-2.2c.3-.3.7-.4 1-.2 1.1.4 2.3.6 3.6.6.6 0 1 .4 1 1V20c0 .6-.4 1-1 1A17 17 0 0 1 3 4c0-.6.4-1 1-1h3.5c.6 0 1 .4 1 1 0 1.3.2 2.5.6 3.6.1.3 0 .7-.2 1z"/></svg>555.014.2301</li>
      <li><svg viewBox="0 0 24 24" aria-hidden="true"><path d="M6 2h12v6H6zM3 9h18v9h-3v4H6v-4H3zm5 7v4h8v-4z"/></svg>555.014.7720</li>
      <li><svg viewBox="0 0 24 24" aria-hidden="true"><path d="M2 5h20v14H2zm2 2v.5l8 5 8-5V7z"/></svg>DPRUETT@kelvardeng.example</li>
    </ul>
    <div class="web-row" style="left:230px;top:244px">
      <span class="divider"></span>
      <span>www.kelvardeng.example</span>
    </div>
  </section>
</main>
</body>
</html>
```